Quarrow financial services, is a financial company that provides consultancy, brokerage services, and funding.

we will be providing the clients with insights, knowledge and data with regards to the financial markets.

with the brokerage services we will try to find the suitable counterparts that provide them with the best investments that suits their needs and expected return.

Target Market(s)

financial institutions, Corporates, high-net worth individuals

Industry/Entity Type

Financial Service

Contact Information for Business Card

Font styles to use
Other font styles liked:
• applemyungjo

Colors
00a990
848484

Requirements
Must have
• the logo at the back
Nice to have
• Finesse
Should not have
• boldness

```html
<!DOCTYPE html>
<html lang="en">
<head>
<meta charset="utf-8">
<title>Quarrow Financial Services — Business Card</title>
<link rel="stylesheet" href="https://fonts.googleapis.com/css2?family=Arimo:wght@400&display=swap">
<style>
  :root {
    --backdrop: #6b5236;
    --card: #0c0c0d;
    --card-edge: #1c1c1e;
    --grey: #848484;
    --grey-light: #a9adb0;
    --teal: #00a990;
    --white: #f2f2f2;
    --mark: #d9ddd6;
  }
  * { box-sizing: border-box; margin: 0; padding: 0; }
  html, body { width: 1200px; height: 858px; overflow: hidden; }
  body {
    background: var(--backdrop);
    display: flex;
    align-items: center;
    justify-content: center;
    gap: 44px;
    font-family: "Arimo", sans-serif;
    font-weight: 400;
  }
  .card {
    width: 540px;
    height: 309px;
    background: linear-gradient(150deg, #1a1a1b 0%, var(--card) 55%, #050505 100%);
    border: 1px solid var(--card-edge);
    box-shadow: 0 18px 40px rgba(0,0,0,.55);
    position: relative;
    color: var(--white);
  }
  .brand {
    display: flex;
    flex-direction: column;
    align-items: flex-start;
  }
  .brand-row {
    display: flex;
    align-items: center;
    gap: 12px;
  }
  .brand-square {
    width: 22px;
    height: 22px;
    background: var(--mark);
    flex: none;
  }
  .brand-name {
    color: var(--grey-light);
    line-height: 1.1;
    white-space: nowrap;
  }
  .tagline {
    color: var(--grey);
    white-space: nowrap;
  }

  /* front */
  .card-front .brand {
    position: absolute;
    left: 36px;
    top: 44px;
  }
  .card-front .brand-name { font-size: 24px; }
  .card-front .tagline { font-size: 11px; margin: 6px 0 0 34px; }
  .contact {
    position: absolute;
    left: 70px;
    top: 150px;
  }
  .contact-name { font-size: 21px; color: var(--white); }
  .contact-role { font-size: 16px; color: var(--teal); margin-bottom: 10px; }
  .contact-line { font-size: 16px; line-height: 1.45; color: var(--white); }

  /* back */
  .card-back .brand {
    position: absolute;
    left: 50%;
    top: 50%;
    transform: translate(-50%, -50%);
  }
  .card-back .brand-square { width: 28px; height: 28px; }
  .card-back .brand-name { font-size: 30px; }
  .card-back .tagline { font-size: 13px; margin: 8px 0 0 40px; }
</style>
</head>
<body>
  <section class="card card-front" aria-label="Business card front">
    <div class="brand">
      <div class="brand-row">
        <span class="brand-square"></span>
        <span class="brand-name">Quarrow Financial Services</span>
      </div>
      <span class="tagline">Clear insight for every investment</span>
    </div>
    <div class="contact">
      <p class="contact-name">Owen Halvik</p>
      <p class="contact-role">owner</p>
      <p class="contact-line">555-014-2870</p>
      <p class="contact-line">info@quarrow.com</p>
      <p class="contact-line">480 N Linden Ave</p>
    </div>
  </section>

  <section class="card card-back" aria-label="Business card back">
    <div class="brand">
      <div class="brand-row">
        <span class="brand-square"></span>
        <span class="brand-name">Quarrow Financial Services</span>
      </div>
      <span class="tagline">Clear insight for every investment</span>
    </div>
  </section>
</body>
</html>
```